Velmora Grove Club Postcard Design

Need a postcard for this business. Go to velmoragroveclub.com to see the product we are selling. Here's another good postcard you can sample. https://www.rowanpilsbydesign.com/?lightbox=dataItem-qz4tunal
Another one: http://blog.tranquet.com/postcard-examples-from-popular-startups/

```html
<!DOCTYPE html>
<html lang="en">
<head>
<meta charset="utf-8">
<title>Velmora Grove Club Postcard</title>
<link href="https://fonts.googleapis.com/css2?family=Poppins:wght@500;600;700;800&family=Montserrat:wght@500;700&display=swap" rel="stylesheet">
<style>
  :root {
    --teal: #3aa19b;
    --teal-dark: #256f6a;
    --terracotta: #b46b57;
    --ink: #141414;
    --paper: #ffffff;
    --stage: #eceeed;
    --photo-warm: #d9c3b3;
    --photo-cool: #e7e7e4;
    --stick: #a65c28;
  }
  * { margin: 0; padding: 0; box-sizing: border-box; }
  html, body { width: 1200px; height: 704px; overflow: hidden; }
  body { background: var(--stage); font-family: "Poppins", sans-serif; color: var(--ink); }

  .postcard {
    position: absolute; left: 135px; top: 14px;
    width: 930px; height: 676px;
    background: var(--paper); overflow: hidden;
    box-shadow: 0 6px 18px rgba(0,0,0,.12);
  }
  .backdrop-photo {
    position: absolute; left: 153px; top: 0; width: 777px; height: 630px;
    background: radial-gradient(ellipse at 60% 35%, var(--photo-warm) 0%, #ece4dd 45%, var(--photo-cool) 75%, #f6f6f5 100%);
    opacity: .75;
  }
  .hero-dog {
    position: absolute; left: 4px; top: 336px; width: 420px; height: 292px;
    background: radial-gradient(ellipse at 55% 55%, #d4d4d4 0%, #a0a0a0 40%, #555 75%, #3a3a3a 100%);
    border-radius: 48% 48% 0 0;
    opacity: .85;
  }
  .title {
    position: absolute; top: 12px; left: 0; width: 100%;
    text-align: center; font-weight: 700; font-size: 30px; letter-spacing: -.3px;
  }
  .feature { position: absolute; top: 76px; width: 320px; margin-left: -160px; text-align: center; }
  .feature-icon { display: block; margin: 0 auto; width: 46px; height: 46px; }
  .feature-heading { margin-top: 8px; font-weight: 600; font-size: 20px; white-space: nowrap; }
  .feature-box {
    position: absolute; top: 98px; left: 55px; width: 209px; height: 158px;
    border-radius: 10px; color: #fff; font-weight: 500; font-size: 16.5px; line-height: 1.2;
    display: flex; flex-direction: column; justify-content: center; align-items: center; text-align: center;
    padding: 8px 10px;
  }
  .feature-box p + p { margin-top: 19px; }
  .box-terracotta { background: var(--terracotta); }
  .box-teal { background: var(--teal); }

  .signup { position: absolute; left: 685px; top: 360px; transform: translateX(-50%); font-weight: 500; font-size: 19px; white-space: nowrap; }
  .ribbon { position: absolute; left: 468px; top: 400px; width: 412px; height: 112px; }
  .ribbon-text {
    position: absolute; left: 685px; top: 406px; transform: translateX(-50%);
    color: #fff; font-weight: 800; font-size: 48px; letter-spacing: 1px; white-space: nowrap;
  }
  .first-month { position: absolute; left: 685px; top: 485px; transform: translateX(-50%); font-weight: 600; font-size: 20px; white-space: nowrap; }
  .treats {
    position: absolute; left: 446px; top: 560px; width: 128px; height: 38px;
    background: linear-gradient(160deg, #c27a3e 0%, var(--stick) 55%, #84461c 100%);
    border-radius: 19px;
  }
  .promo { position: absolute; left: 672px; top: 532px; transform: translateX(-50%); text-align: center; font-family: "Montserrat", sans-serif; line-height: 1.25; }
  .promo-label { color: var(--teal); font-size: 18px; font-weight: 500; }
  .promo-code { font-size: 21px; font-weight: 700; }

  .brand {
    position: absolute; left: 794px; top: 520px; width: 113px; height: 113px; z-index: 2;
    border-radius: 50%; border: 3px solid var(--ink); background: #fff;
    display: flex; align-items: center; justify-content: center; text-align: center;
    font-weight: 700; font-size: 14px; line-height: 1.15; padding: 10px;
  }

  .benefits {
    position: absolute; left: 0; top: 628px; width: 100%; height: 48px;
    background: var(--teal); display: flex; align-items: center; justify-content: space-between;
    padding: 0 15px; font-weight: 500; font-size: 17px; white-space: nowrap;
  }
  .benefit-light { color: #fff; }
  .benefit-dark { color: var(--ink); }
</style>
</head>
<body>
  <main class="postcard">
    <div class="backdrop-photo" role="img" aria-label="Soft faded photo of a tricolour dog looking at the viewer"></div>

    <h1 class="title">Top Quality &amp; Healthy Bully Sticks For Your Dog</h1>

    <section class="feature" style="left:155px">
      <svg class="feature-icon" viewBox="0 0 46 46" aria-hidden="true">
        <path d="M44 44H23A21 21 0 1 1 44 23Z" fill="var(--teal)"/>
        <path d="M14 23l6 7 12-14" stroke="#fff" stroke-width="4.5" fill="none" stroke-linecap="round" stroke-linejoin="round"/>
      </svg>
      <h2 class="feature-heading">Doggy joy guarantee</h2>
      <div class="feature-box box-terracotta">
        <p>12 Pack of bully sticks</p><p>Monthly charging</p><p>Cancel anytime</p>
      </div>
    </section>

    <section class="feature" style="left:470px">
      <svg class="feature-icon" viewBox="0 0 46 46" aria-hidden="true">
        <path d="M44 44H23A21 21 0 1 1 44 23Z" fill="var(--teal)"/>
        <path d="M23 31c-8-5-11-9-11-12.5a5 5 0 0 1 11-2 5 5 0 0 1 11 2C34 22 31 26 23 31z" fill="#fff"/>
      </svg>
      <h2 class="feature-heading">Sourced from free range cattle</h2>
      <div class="feature-box box-teal">
        <p>Humanely made without added hormones, antibiotics or steroids</p><p>All-natural</p>
      </div>
    </section>

    <section class="feature" style="left:774px">
      <svg class="feature-icon" viewBox="0 0 46 46" aria-hidden="true">
        <path d="M44 44H23A21 21 0 1 1 44 23Z" fill="var(--teal)"/>
        <path d="M23 12l-11 10h3v10h6v-6h4v6h6V22h3z" fill="#fff"/>
      </svg>
      <h2 class="feature-heading">Shipped to your doorstep</h2>
      <div class="feature-box box-terracotta" style="top:96px">
        <p>We ship worldwide and inside the United States; Asia, Africa, North America, South America, Antarctica, Europe and Australia</p>
      </div>
    </section>

    <div class="hero-dog" role="img" aria-label="Photo of a black and white French bulldog looking up"></div>

    <p class="signup">Sign up for a subscription &amp;</p>
    <svg class="ribbon" viewBox="0 0 412 112" aria-hidden="true">
      <path d="M0 52l52-14 16 54-46 12 6-22z" fill="var(--teal)"/>
      <path d="M412 52l-52-14-16 54 46 12-6-22z" fill="var(--teal)"/>
      <path d="M38 30Q206 -8 374 30l-10 50Q206 46 48 80z" fill="var(--teal)"/>
      <path d="M48 80l20 12-6-20zM364 80l-20 12 6-20z" fill="var(--teal-dark)"/>
    </svg>
    <p class="ribbon-text">SAVE 50%</p>
    <p class="first-month">on your first month</p>

    <div class="treats" role="img" aria-label="Photo of two crossed bully sticks"></div>
    <div class="promo">
      <p class="promo-label">USE CODE:</p>
      <p class="promo-code">BULLYSTICKS</p>
      <p class="promo-label">AT CHECKOUT</p>
    </div>

    <footer class="benefits">
      <span class="benefit-light">Chemical Free</span>
      <span class="benefit-dark">Promotes Oral Health</span>
      <span class="benefit-light">Provides stress relief</span>
      <span class="benefit-dark">Low in fat</span>
      <span class="benefit-light">High in protein</span>
      <span class="benefit-dark">100% digestible</span>
    </footer>

    <div class="brand">Velmora Grove Club</div>
  </main>
</body>
</html>
```